Business Card Design Project

We consult with hotels on setting rates and maximizing a revenue strategy

Industry/Entity Type

Business

Contact Information for Business Card

I am not sure what I want. Our company offers high level consulting to hotels around the country but we are also laid back. I would like something that is professional but also shows the laid back side

```html
<!DOCTYPE html>
<html lang="en">
<head>
<meta charset="utf-8">
<title>Rivergate Business Card</title>
<link rel="stylesheet" href="https://fonts.googleapis.com/css2?family=Archivo:ital,wght@0,400;0,700;1,400&display=swap">
<style>
  :root {
    --backdrop: #221f1e;
    --teal: #00858a;
    --teal-deep: #006b70;
    --paper: #f4f4f2;
    --ink: #2b2b2b;
    --grey: #6f6f6f;
    --white: #ffffff;
  }
  * { margin: 0; padding: 0; box-sizing: border-box; }
  html, body {
    width: 1200px; height: 814px; overflow: hidden;
    background: var(--backdrop);
    font-family: "Archivo", Arial, sans-serif;
  }
  .sheet {
    position: relative; width: 1200px; height: 814px;
    display: flex; align-items: center; justify-content: center; gap: 60px;
  }
  .card {
    position: relative; width: 460px; height: 263px;
    border-radius: 3px;
    box-shadow: 0 14px 34px rgba(0,0,0,.45);
  }
  .card--front { background: var(--teal); }
  .card--back { background: var(--paper); }

  .wordmark { display: flex; align-items: center; gap: 8px; }
  .wordmark__square { width: 12px; height: 12px; flex: none; }
  .wordmark__name {
    font-weight: 700; text-transform: uppercase; line-height: 1.15;
    letter-spacing: .02em;
  }
  .card--front .wordmark {
    position: absolute; left: 50%; top: 50%; transform: translate(-50%, -50%);
  }
  .card--front .wordmark__square { background: var(--white); }
  .card--front .wordmark__name { color: var(--white); font-size: 17px; }
  .card--front .wordmark__tag { display: block; font-size: 9px; letter-spacing: .04em; }

  .card--back .wordmark { position: absolute; left: 24px; top: 30px; }
  .card--back .wordmark__square { background: var(--teal); width: 10px; height: 10px; }
  .card--back .wordmark__name { color: var(--teal); font-size: 13px; }
  .card--back .wordmark__tag { display: block; font-size: 7px; letter-spacing: .04em; }

  .contact {
    position: absolute; left: 220px; top: 92px;
    font-size: 11px; letter-spacing: .14em; color: var(--grey);
    line-height: 1.7;
  }
  .contact__name { color: var(--ink); font-weight: 700; letter-spacing: .2em; font-size: 11px; }
  .contact__title { font-style: italic; margin-bottom: 2px; }
  .contact__row { display: flex; gap: 8px; }
  .contact__label { color: var(--teal); font-weight: 700; width: 14px; }
</style>
</head>
<body>
<main class="sheet">
  <section class="card card--front" aria-label="Card front">
    <div class="wordmark">
      <span class="wordmark__square"></span>
      <span class="wordmark__name">Rivergate<span class="wordmark__tag">Revenue Management Solutions</span></span>
    </div>
  </section>

  <section class="card card--back" aria-label="Card back">
    <div class="wordmark">
      <span class="wordmark__square"></span>
      <span class="wordmark__name">Rivergate<span class="wordmark__tag">Revenue Management Solutions</span></span>
    </div>
    <div class="contact">
      <p class="contact__name">MARA ELLISON</p>
      <p class="contact__title">Regional Revenue Manager</p>
      <p class="contact__row"><span class="contact__label">P.</span>503-555-0142</p>
      <p class="contact__row"><span class="contact__label">F.</span>503-555-0187</p>
      <p class="contact__row"><span class="contact__label">E.</span>mara@rivergaterms.com</p>
      <p class="contact__row"><span class="contact__label">W.</span>rivergaterms.com</p>
    </div>
  </section>
</main>
</body>
</html>
```